Postcard Design January 2015

I need a postcard designed to introduce my company to potential new customers in the UK. My company is TW Page Services based in Chester and we represent one of Poland's leading and long established book printers. We offer competitive pricing, consistently high levels of print and binding quality and industry leading levels of customer service. We have been meeting the print requirements of UK publishers for more than 10 years.
Updates

Industry/Entity Type

Industry

```html
<!DOCTYPE html>
<html lang="en">
<head>
<meta charset="utf-8">
<title>TW Page Services – Postcard</title>
<link rel="stylesheet" href="https://fonts.googleapis.com/css2?family=Libre+Baskerville:wght@400;700&family=Sorts+Mill+Goudy&display=swap">
<style>
  :root {
    --taupe: #a5978c;
    --wine: #8a2f2b;
    --band: #4b2b1d;
    --ink-dark: #3b2217;
    --ink-light: #fbf6ef;
    --brand: #8f2a24;
    --frame: #f4f1ec;
  }
  * { margin: 0; padding: 0; box-sizing: border-box; }
  html, body { width: 1200px; height: 929px; overflow: hidden; }
  body { background: var(--taupe); font-family: "Libre Baskerville", Georgia, serif; }
  .postcard { position: relative; width: 1200px; height: 929px; background: var(--taupe); overflow: hidden; }
  .side-band { position: absolute; left: 955px; top: 0; width: 245px; height: 929px; background: var(--wine); }
  .floor-band { position: absolute; left: 0; top: 612px; width: 1200px; height: 48px; background: var(--band); }

  .brand { position: absolute; left: 40px; top: 60px; width: 330px; }
  .brand-name { font-family: "Libre Baskerville", Georgia, serif; font-weight: 700; color: var(--brand); font-size: 44px; line-height: 1.15; }
  .brand-mark { display: inline-block; width: 18px; height: 18px; background: var(--brand); margin-bottom: 12px; }

  .services { position: absolute; left: 400px; top: 130px; font-family: "Sorts Mill Goudy", Georgia, serif; color: var(--ink-light); font-size: 31px; line-height: 40px; text-shadow: 2px 2px 3px rgba(40,20,10,.8); }

  .intro { position: absolute; left: 190px; top: 282px; width: 790px; text-align: center; font-weight: 700; color: var(--ink-light); font-size: 23px; line-height: 36px; text-shadow: 1px 1px 2px rgba(40,20,10,.6); }

  .benefits { position: absolute; left: 500px; top: 430px; width: 540px; text-align: center; color: var(--ink-dark); }
  .benefits h2 { font-size: 25px; line-height: 38px; font-weight: 700; }
  .benefits ul { list-style: none; font-size: 22px; line-height: 36px; }

  .photo { position: absolute; box-shadow: 3px 3px 8px rgba(30,15,8,.45); }
  .photo-factory { left: 828px; top: 36px; width: 333px; height: 262px; background: linear-gradient(160deg, #c9ccd0, #6e7479 60%, #3f4448); }
  .photo-conveyor { left: 173px; top: 468px; width: 244px; height: 144px; background: linear-gradient(120deg, #e3e0dc, #9aa0a6 55%, #b75a8a); }
  .photo-swatches { left: 36px; top: 612px; width: 232px; height: 162px; border: 6px solid var(--frame); background: linear-gradient(135deg, #e84a3a, #f3c23a 30%, #4fb36b 55%, #3a6fc4 80%, #f0f0f0); }
  .photo-bound { left: 307px; top: 612px; width: 193px; height: 171px; background: linear-gradient(90deg, #e8e8e8, #8b9096 50%, #d9dadb); }
  .photo-machine { left: 164px; top: 715px; width: 238px; height: 178px; background: linear-gradient(150deg, #d8d2c6, #8d8274 55%, #4c463e); }
  .photo-book { left: 900px; top: 581px; width: 193px; height: 274px; background: linear-gradient(160deg, #f2ede3, #c9bda7 50%, #5e5040); }
</style>
</head>
<body>
<main class="postcard">
  <div class="side-band"></div>
  <div class="floor-band"></div>

  <div class="brand">
    <span class="brand-mark"></span>
    <div class="brand-name">TW Page Services</div>
  </div>

  <p class="services">Litho &amp; Digital Printing,<br>Bookbinding &amp; Finishing</p>

  <div class="photo photo-factory" role="img" aria-label="Photo of a large book printing factory floor"></div>

  <p class="intro">TW Page Services offer a competitive service to book publishers looking for excellence in book printing and binding, combined with a first rate service.</p>

  <section class="benefits">
    <h2>Our customers enjoy:</h2>
    <ul>
      <li>· High quality book printing and binding</li>
      <li>· Competitive pricing</li>
      <li>· Excellent customer service</li>
    </ul>
  </section>

  <div class="photo photo-conveyor" role="img" aria-label="Photo of printed sheets moving along a press conveyor"></div>
  <div class="photo photo-swatches" role="img" aria-label="Photo of a fanned colour swatch guide"></div>
  <div class="photo photo-bound" role="img" aria-label="Photo of stacks of bound book blocks"></div>
  <div class="photo photo-machine" role="img" aria-label="Photo of a bookbinding machine"></div>
  <div class="photo photo-book" role="img" aria-label="Photo of an open book with fanned pages"></div>
</main>
</body>
</html>
```